Nutritional supplement business needs a label design

The product is an Omega 3 fish oil capsules, in a transparent round pet bottle with white cap.
The capsules are translucent yellow. The dimensions of the bottle are height 13 cm and width 6.5 cm.
The label size should be is 62mm height and 186mm length.

The final desing should be modern, clean and communicate a execellnt quality product.
Updates

Reason: Hi, we decided to extend the deadline because there were two rest days in the middle of the project and with this extention, the designers will have a full working week to develop their ideas. Thank you.

Target Market(s)

Women and Men, ages 30 to 65, medium to medium-low income. The product will be displayed in the walk around shelves in "value-price" pharmacies

Industry/Entity Type

Health And Wellness

Font styles to use
Sans Serif

Requirements
Must have
• A salmon like vector "modern" "stylish"
Nice to have
• A "seal" to highlight a benefit in metallic gold
Should not have
• Any body parts or body organs such as heart. Any reference that the product treats or cures any disease.

```html
<!DOCTYPE html>
<html lang="es">
<head>
<meta charset="UTF-8">
<title>Nordavia Omega-3 Label</title>
<link rel="stylesheet" href="https://fonts.googleapis.com/css2?family=Montserrat:wght@400;500;600;700;800&display=swap">
<style>
  :root {
    --bg: #f1f2f4;
    --label-white: #f7f8f9;
    --navy: #15246b;
    --navy-band: #0f1f63;
    --blue-light: #63b4ea;
    --blue-mid: #3f98dd;
    --blue-deep: #2a7fcf;
    --gold-dark: #7a4e12;
    --gold: #c8912e;
    --gold-light: #f3d27a;
    --brand-green: #3f9a3c;
    --rule: #b9c0cc;
    --fish-blue: #4aa3dc;
  }
  * { box-sizing: border-box; margin: 0; padding: 0; }
  html, body { width: 964px; height: 1200px; overflow: hidden; }
  body {
    background: var(--bg);
    font-family: "Montserrat", Arial, sans-serif;
    position: relative;
  }
  .label {
    position: absolute;
    left: 216px; top: 324px;
    width: 533px; height: 552px;
    background: var(--label-white);
    overflow: hidden;
  }
  .label__top-stripe {
    position: absolute; left: 0; top: 0; width: 100%; height: 14px;
    background: linear-gradient(90deg, var(--gold-dark), var(--gold) 30%, var(--gold-light) 55%, var(--gold) 75%, var(--gold-dark));
  }
  .brand {
    position: absolute; left: 0; top: 70px; width: 100%;
    display: flex; justify-content: center; align-items: center; gap: 10px;
  }
  .brand__name {
    font-weight: 700; font-size: 30px; color: var(--navy); letter-spacing: 0.3px;
  }
  .brand__dot {
    width: 22px; height: 22px; border-radius: 50%; background: var(--brand-green);
  }
  .product-name {
    position: absolute; left: 16px; top: 150px;
    font-weight: 500; font-size: 74px; line-height: 1; color: var(--navy); letter-spacing: -1px;
  }
  .product-type {
    position: absolute; left: 74px; top: 229px; width: 274px; height: 48px;
    border: 2px solid var(--navy); border-radius: 3px;
    display: flex; flex-direction: column; justify-content: center; align-items: center;
    font-weight: 500; font-size: 18px; line-height: 1.1; color: var(--navy);
  }
  .fish-art {
    position: absolute; left: 372px; top: 212px; width: 120px; height: 150px;
    border-radius: 50%;
    background: radial-gradient(ellipse at 50% 45%, #8ccaee, var(--fish-blue) 70%);
  }
  .dose {
    position: absolute; left: 24px; top: 322px; display: flex; align-items: center;
  }
  .dose__total { font-weight: 500; font-size: 36px; color: var(--navy); }
  .dose__divider { width: 2px; height: 50px; background: var(--navy); margin: 0 12px 0 16px; }
  .dose__active { font-weight: 500; font-size: 17px; line-height: 1.15; color: var(--navy); }
  .rule {
    position: absolute; left: 16px; top: 380px; width: 366px; height: 2px; background: var(--rule);
  }
  .blue-panel {
    position: absolute; left: 0; top: 451px; width: 100%; height: 101px;
    background: linear-gradient(180deg, var(--blue-light), var(--blue-mid) 55%, var(--blue-deep));
  }
  .blue-panel svg { position: absolute; inset: 0; }
  .net-content {
    position: absolute; left: 0; top: 522px; width: 538px; text-align: center;
    font-weight: 600; font-size: 12.5px; color: #ffffff; letter-spacing: 0.2px;
  }
  .premium-band {
    position: absolute; left: 0; top: 427px; width: 400px; height: 24px;
    background: var(--navy-band);
    display: flex; align-items: center; justify-content: center;
    padding-left: 150px;
    font-weight: 500; font-size: 15px; letter-spacing: 3px; color: #ffffff;
  }
  .seal {
    position: absolute; left: 404px; top: 384px; width: 116px; height: 116px;
    border-radius: 50%;
    background: radial-gradient(circle at 40% 35%, var(--gold-light), var(--gold) 55%, var(--gold-dark));
  }
</style>
</head>
<body>
  <section class="label">
    <div class="label__top-stripe"></div>

    <div class="brand">
      <span class="brand__name">Nordavia</span>
      <span class="brand__dot"></span>
    </div>

    <h1 class="product-name">OMEGA-3</h1>

    <div class="product-type">
      <span>ACEITE DE PESCADO</span>
      <span>DE AGUA FRIA</span>
    </div>

    <div class="fish-art" role="img" aria-label="Stylised blue salmon illustration leaping upward"></div>

    <div class="dose">
      <span class="dose__total">1,000mg</span>
      <span class="dose__divider"></span>
      <span class="dose__active">300mg Active<br>Omega-3</span>
    </div>

    <div class="rule"></div>

    <div class="blue-panel">
      <svg width="533" height="101" viewBox="0 0 533 101" aria-hidden="true">
        <path d="M0 40 C120 10 220 70 340 40 S 480 20 533 35 L533 101 L0 101 Z" fill="#ffffff" opacity="0.10"/>
        <path d="M0 70 C140 45 260 95 380 65 S 500 55 533 62 L533 101 L0 101 Z" fill="#ffffff" opacity="0.08"/>
      </svg>
    </div>

    <div class="premium-band">PREMIUM FISH OIL</div>

    <div class="net-content">CONTENIDO NETO&nbsp; 100 CÁPSULAS</div>

    <div class="seal" role="img" aria-label="Metallic gold quality seal"></div>
  </section>
</body>
</html>
```